Rack Card for Charter Sail Boat business in SF Bay

We are in need of a rack card design to highlight the business to tourists and locals. 2 sided card 3.86" x 8.39" (full bleed)

We are looking for visually appleaing designs on the front and back but a little more detail on the back.

Use the info provided (text and info) on the website to include the 3 key services (Quick, 1/2 day, fullday) and aspects of the boat, location and other key info for customers (not prices). DO NOT INCLUDE ALL THIS TEXT please pick the elements you would like to fit your design and inform the customer as you would like about the business.

I can also provide photos directly from the video if you think those would fit your design. If video doesn't work on this upload you can view it at the website or facebook page (www.fb.com/tidewrenllc)

Now included a few video pictures in files for your use

Target Market(s)

Tourists and locals to san francisco east bay. 25 - 55 years old. Men and women.

Industry/Entity Type

Entertainment

Colors
0455a3
ec1f27
f3f1f8

Requirements
Must have
• Highlight services, key contact information (email, phone, website site), Visual impact
• 2-sided card - 3.86" x 8.39" (98 x 213 mm)
Nice to have
• facebook link, electric engine(green),

```html
<!DOCTYPE html>
<html lang="en">
<head>
<meta charset="utf-8">
<title>TideWren Rack Card</title>
<link href="https://fonts.googleapis.com/css2?family=Montserrat:ital,wght@0,400;0,500;0,700;1,700&family=Tinos:ital@1&display=swap" rel="stylesheet">
<style>
  :root {
    --brand-blue: #2f56a5;
    --brand-blue-deep: #1f3f86;
    --ink: #1d2230;
    --paper: #f3f1f8;
    --sky-top: #c9d3e6;
    --sky-mid: #e4e8f1;
    --water: #55708f;
    --water-deep: #34506f;
    --stage: #e9e9ea;
    --accent-red: #ec1f27;
  }
  * { box-sizing: border-box; margin: 0; padding: 0; }
  html, body { width: 1200px; height: 1200px; overflow: hidden; }
  body {
    background: var(--stage);
    position: relative;
    font-family: "Montserrat", sans-serif;
    color: var(--ink);
  }
  .card {
    position: absolute;
    background: var(--brand-blue);
    overflow: hidden;
  }
  .card-inner { position: absolute; left: 14px; top: 14px; right: 14px; bottom: 56px; overflow: hidden; }
  .card-footer {
    position: absolute; left: 0; right: 0; bottom: 0; height: 56px;
    background: var(--brand-blue);
    color: #fff; font-weight: 500; font-size: 29px; letter-spacing: 1.5px;
    display: flex; align-items: center;
  }

  /* Back side */
  .card-back { left: 238px; top: 58px; width: 490px; height: 1022px; z-index: 1; }
  .card-back .card-inner {
    background: linear-gradient(180deg, var(--sky-mid) 0%, #dfe4ee 40%, #c9d2df 56%, var(--water) 60%, var(--water-deep) 75%, #7f93aa 88%, #c6cfdb 100%);
  }
  .back-headline { position: absolute; left: 0; width: 462px; top: 40px; text-align: center; font-size: 24px; line-height: 33px; letter-spacing: 0.5px; font-weight: 400; }
  .brand-name { color: var(--brand-blue); font-weight: 700; font-style: italic; }
  .back-points { position: absolute; left: 44px; top: 116px; list-style: none; font-family: "Tinos", serif; font-style: italic; font-size: 21px; line-height: 25px; letter-spacing: 1px; white-space: nowrap; }
  .back-points li { margin-bottom: 13px; }
  .back-points .marker { font-style: normal; margin-left: -20px; margin-right: 4px; }
  .photo-frame {
    position: absolute; left: 26px; top: 385px; width: 240px; height: 232px;
    border: 4px solid #fff;
    background: linear-gradient(180deg, #b9c7dd 0%, #d7e0ec 30%, #9fb2c6 42%, #6f8aa0 65%, #5b7a86 100%);
  }
  .back-tagline { position: absolute; left: 34px; top: 650px; font-size: 24px; line-height: 31px; letter-spacing: 0.8px; white-space: nowrap; color: #1d2230; }
  .back-tagline .brand-name { color: #3b63b8; font-style: normal; }
  .back-places { position: absolute; left: 34px; top: 730px; list-style: none; font-family: "Tinos", serif; font-style: italic; font-size: 19px; white-space: nowrap; }
  .back-places li { margin-bottom: 11px; display: flex; align-items: center; gap: 10px; }
  .back-mark { position: absolute; left: 122px; top: 850px; display: flex; align-items: center; gap: 8px; color: var(--brand-blue); font-weight: 700; font-size: 22px; }
  .back-mark .dot { width: 22px; height: 22px; border-radius: 50%; background: var(--brand-blue); }
  .card-back .card-footer { padding-left: 112px; }

  /* Front side */
  .card-front { left: 428px; top: 130px; width: 485px; height: 1014px; z-index: 2; }
  .card-front .card-inner {
    background: linear-gradient(180deg, var(--sky-top) 0%, var(--sky-mid) 30%, #eef0f5 55%, #d3d9e2 62%, #c4ccd7 72%, #dfe3ea 100%);
  }
  .front-title { position: absolute; left: 0; right: 0; top: 30px; text-align: center; font-size: 29px; letter-spacing: 0.8px; font-weight: 400; }
  .section-band { position: absolute; left: 0; width: 338px; height: 39px; }
  .section-band svg { position: absolute; inset: 0; }
  .section-band span { position: relative; display: block; padding-left: 30px; line-height: 39px; color: #fff; font-weight: 700; font-size: 28px; letter-spacing: 1px; }
  .section-copy { position: absolute; left: 30px; width: 412px; font-family: "Tinos", serif; font-style: italic; font-size: 16.2px; line-height: 20.5px; }
  .section-copy p + p { margin-top: 6px; }
  .section-copy .brand-inline { color: var(--brand-blue); font-weight: 700; }
  .packages-tab { position: absolute; left: 14px; top: 730px; width: 182px; height: 34px; background: var(--brand-blue); border-radius: 8px 8px 0 0; color: #fff; font-weight: 700; font-size: 26px; letter-spacing: 0.5px; padding-left: 18px; line-height: 40px; }
  .packages-box { position: absolute; left: 14px; top: 762px; width: 434px; height: 172px; background: var(--brand-blue); border-radius: 0 8px 8px 8px; color: #fff; padding: 10px 10px 0 16px; }
  .package { font-size: 14.5px; line-height: 18px; letter-spacing: 0.2px; padding-bottom: 8px; }
  .package + .package { border-top: 1px solid rgba(255,255,255,0.6); padding-top: 9px; }
  .package-name { font-weight: 700; text-decoration: underline; font-size: 17px; }
  .card-front .card-footer { justify-content: center; }
</style>
</head>
<body>

<section class="card card-back" aria-label="Rack card, back side">
  <div class="card-inner">
    <h2 class="back-headline">Come Abord <span class="brand-name">TideWren</span> and view<br><span style="padding-right:210px">San Franc</span></h2>
    <ul class="back-points">
      <li><span class="marker">&gt;</span>Supreme blue<br>all the modern<br>entertainment</li>
      <li><span class="marker">&gt;</span>Located in Be<br>access from E<br>Valley.</li>
      <li><span class="marker">&gt;</span>We love to sh<br>family how to<br>having fun.</li>
    </ul>
    <div class="photo-frame" role="img" aria-label="Photo of the Golden Gate Bridge seen across sparkling bay water"></div>
    <p class="back-tagline"><span class="brand-name">TideWren</span> is y<br>as you wish w</p>
    <ul class="back-places">
      <li><svg width="12" height="10" viewBox="0 0 12 10"><path d="M0 0 L12 5 L0 10 L3 5 Z" fill="#2f56a5"/></svg>San Francisco Ba</li>
      <li><svg width="12" height="10" viewBox="0 0 12 10"><path d="M0 0 L12 5 L0 10 L3 5 Z" fill="#2f56a5"/></svg>Golden Gate Bri</li>
    </ul>
    <div class="back-mark"><span class="dot"></span>TideWren</div>
  </div>
  <footer class="card-footer">fb.com/tidewrenllc</footer>
</section>

<section class="card card-front" aria-label="Rack card, front side">
  <div class="card-inner">
    <h1 class="front-title">Experience <span class="brand-name">TideWren</span></h1>

    <div class="section-band" style="top:79px">
      <svg width="338" height="39" viewBox="0 0 338 39"><path d="M0 0 H338 L325 39 H0 Z" fill="#2f56a5"/></svg>
      <span>MODERN</span>
    </div>
    <div class="section-copy" style="top:130px">
      <p><span class="brand-inline">TideWren</span> is completle electric (which means no diesel smells, noise or vibrations to suffer).</p>
      <p>New electrics, plumbing, toilets, and deck areas compliment the elegant lines and features of this Harlow Pierce 46 foot cutter rigged sailboat.</p>
    </div>

    <div class="section-band" style="top:255px">
      <svg width="338" height="39" viewBox="0 0 338 39"><path d="M0 0 H338 L325 39 H0 Z" fill="#2f56a5"/></svg>
      <span>ENTERTAINMENT</span>
    </div>
    <div class="section-copy" style="top:306px">
      <p>While being surrounded by beauty and wonder of San Francisco Bay, enjoy your choice of music from your source, StarWave XM, CD or Old School FM.</p>
      <p>Enjoy the refreshments and snacks provided by us or have lunch/dinner on a private beach!</p>
    </div>

    <div class="section-band" style="top:434px">
      <svg width="338" height="39" viewBox="0 0 338 39"><path d="M0 0 H338 L325 39 H0 Z" fill="#2f56a5"/></svg>
      <span>SAFE</span>
    </div>
    <div class="section-copy" style="top:485px">
      <p>The safety of everyone aboard TideWren is paramount to our business and your enjoyment. We carry aboard everything to make your time aboard safe.</p>
    </div>

    <div class="section-band" style="top:562px">
      <svg width="338" height="39" viewBox="0 0 338 39"><path d="M0 0 H338 L325 39 H0 Z" fill="#2f56a5"/></svg>
      <span>THE TRIP</span>
    </div>
    <div class="section-copy" style="top:612px">
      <p>When chartering TideWren, the vessel is yours to direct anywhere within the time you wish to enjoy her, but we do have a few old favorites that are always fun!</p>
      <p>Our custom trips are simple to arrange and book, we simply ask for a minimum of 3 hours duration.</p>
    </div>

    <div class="packages-tab">PACKAGES</div>
    <div class="packages-box">
      <p class="package"><span class="package-name">2 hour Blast:</span> Sunset sail or an early morning cruise or a blast out into the bay.</p>
      <p class="package"><span class="package-name">Half Day Fun:</span> A full morning, afternoon or evening out in the Bay.</p>
      <p class="package"><span class="package-name">Full Day Adventure:</span> The day includes a complete circuit of the Bay and lunch at anchor</p>
    </div>
  </div>
  <footer class="card-footer">sailtidewren.com</footer>
</section>

</body>
</html>
```